Judicial election website to attract voters

I need a simple one-page web design for a judicial election. I'm going to put up one picture, maybe two. The picture I have needs a little touch-up (whiten teeth for example). I have 3 paragraphs of text. I'd like a "Donate" button that can link to a CoinDrift account. I'd also like a little background design, like the Constitution or something like that. There's a couple other little things but that's the bulk of it.

Target Market(s)

Involved voters and some media

Industry/Entity Type

Legal

Number of Pages Required

1 page

Font styles to use
Sans Serif

Requirements
Must have
• My picture, text, donate button
• Phrase "Remember to vote August 30, 2016!"
Nice to have
• Perhaps a second photo, maybe a short 30 second video of me talking directly to the voters, cool background: Constitution, something judgey.
Should not have
• Not sure ... profanity, I guess.

```html
<!DOCTYPE html>
<html lang="en">
<head>
<meta charset="utf-8">
<title>Local Election</title>
<link href="https://fonts.googleapis.com/css2?family=Josefin+Sans:wght@400;600&family=Lato:wght@400;700&display=swap" rel="stylesheet">
<style>
  :root {
    --accent: #f45f3c;
    --ink: #333333;
    --slate: #5a6272;
    --rule: #c9c9c9;
    --divider: #ececec;
    --footer: #000000;
    --white: #ffffff;
  }
  * { box-sizing: border-box; margin: 0; padding: 0; }
  html, body { width: 1200px; height: 933px; overflow: hidden; background: var(--white); }
  body { position: relative; font-family: 'Lato', sans-serif; color: var(--ink); }

  .top-bar { position: absolute; top: 0; left: 0; width: 1200px; height: 3px; background: var(--accent); }
  .site-header { position: absolute; top: 3px; left: 0; width: 1200px; height: 77px; display: flex; align-items: center; justify-content: center; }
  .brand { font-family: 'Josefin Sans', sans-serif; font-size: 29px; font-weight: 400; letter-spacing: 0.5px; color: var(--slate); padding-top: 8px; }
  .brand span { color: var(--accent); }

  .hero { position: absolute; top: 80px; left: 0; width: 1200px; height: 472px; overflow: hidden; }
  .hero-photo { position: absolute; inset: 0;
    background:
      radial-gradient(ellipse 260px 300px at 1040px 260px, #d08a78 0%, #c67a69 40%, rgba(198,122,105,0) 75%),
      linear-gradient(90deg, #4a1a22 0%, #5c2430 30%, #8a5a4a 52%, #c8b8a8 66%, #d9c8b6 78%, #d7805f 100%);
  }
  .hero-photo::after { content: ""; position: absolute; left: 0; right: 0; top: 0; height: 90px;
    background: linear-gradient(180deg, rgba(120,70,60,0.45), rgba(120,70,60,0)); }
  .vote-banner { position: absolute; left: 99px; top: 276px; height: 49px; padding: 0 24px 0 22px;
    background: var(--accent); border-left: 4px solid var(--white);
    font-family: 'Josefin Sans', sans-serif; font-size: 28px; color: var(--white);
    display: flex; align-items: center; padding-top: 5px; }
  .slider-dots { position: absolute; top: 517px; left: 571px; display: flex; gap: 8px; }
  .slider-dots span { width: 14px; height: 14px; border-radius: 50%; border: 2px solid var(--white); }
  .slider-dots span.active { background: var(--accent); border-color: var(--accent); }

  .column { position: absolute; top: 583px; }
  .col-about { left: 99px; width: 272px; }
  .col-video { left: 471px; width: 272px; }
  .col-points { left: 846px; width: 254px; }
  .divider { position: absolute; top: 583px; width: 1px; height: 265px; background: var(--divider); }

  .column h2 { font-family: 'Josefin Sans', sans-serif; font-weight: 400; font-size: 23px; color: var(--accent); height: 45px; padding-top: 9px; position: relative; border-bottom: 1px solid var(--rule); }
  .column h2::after { content: ""; position: absolute; left: 0; bottom: -1px; width: 64px; height: 2px; background: var(--accent); }

  .about-text { margin-top: 16px; font-size: 14px; line-height: 22px; letter-spacing: 0.4px; }

  .video-frame { margin-top: 11px; width: 279px; height: 201px; border: 1px solid #e3e3e3; padding: 4px; position: relative; left: -1px; }
  .video-still { width: 100%; height: 100%; background: linear-gradient(120deg, #2a3038 0%, #3c4350 40%, #b9a79a 62%, #e8e2da 80%, #5a3a20 100%); position: relative; }
  .play-button { position: absolute; left: 50%; top: 50%; transform: translate(-50%, -50%); }

  .point-list { list-style: none; margin-top: 17px; }
  .point-list li { display: flex; align-items: center; height: 32.6px; font-size: 13.5px; }
  .point-list svg { margin-right: 12px; flex-shrink: 0; }

  .site-footer { position: absolute; top: 883px; left: 0; width: 1200px; height: 50px; background: var(--footer); }
  .copyright { position: absolute; left: 99px; top: 17px; font-family: 'Josefin Sans', sans-serif; font-size: 14px; color: var(--white); }
  .donate-button { position: absolute; left: 993px; top: 8px; width: 108px; height: 35px; background: var(--accent); border: 2px solid var(--white);
    color: var(--white); font-family: 'Josefin Sans', sans-serif; font-size: 15px; display: flex; align-items: center; justify-content: center; padding-top: 3px; text-decoration: none; }
</style>
</head>
<body>
  <div class="top-bar"></div>
  <header class="site-header">
    <div class="brand">LOREM <span>IPSUM</span></div>
  </header>

  <section class="hero">
    <div class="hero-photo" role="img" aria-label="Photo of a wooden judge's gavel on a desk with a smiling candidate portrait on the right"></div>
    <div class="vote-banner">Remember To Vote August 30, 2016!</div>
    <div class="slider-dots"><span></span><span class="active"></span><span></span></div>
  </section>

  <div class="divider" style="left:422px"></div>
  <div class="divider" style="left:795px"></div>

  <section class="column col-about">
    <h2>Lorem Ipsum Dolor</h2>
    <p class="about-text">Lorem ipsum dolor sit amet, consectetuer adipiscing elit, sed diam nonummy nibh euismod tincidunt ut laoreet dolore magna aliquam erat volutpat. Ut wisi enim ad minim veniam, quis nostrud exerci exerci tation ullamcorper suscipit lobortis nisl ut aliquip ex ea commodo consequat. Duis autem vel eum iriure dolor in hendrerit Duis autem vel eum iriure dolor in hendrerit.</p>
  </section>

  <section class="column col-video">
    <h2>Lorem Ipsum Dolor</h2>
    <div class="video-frame">
      <div class="video-still" role="img" aria-label="Video still of a man in a suit signing documents at a desk">
        <svg class="play-button" width="50" height="50" viewBox="0 0 50 50" aria-hidden="true">
          <circle cx="25" cy="25" r="24" fill="rgba(0,0,0,0.55)"/>
          <path d="M20 15 L35 25 L20 35 Z" fill="#ffffff"/>
        </svg>
      </div>
    </div>
  </section>

  <section class="column col-points">
    <h2>Lorem Ipsum Dolor</h2>
    <ul class="point-list">
      <li><svg width="15" height="12" viewBox="0 0 15 12"><path d="M1 6.5 L5.5 10.5 L14 1.5" fill="none" stroke="#f45f3c" stroke-width="3" stroke-linecap="round" stroke-linejoin="round"/></svg>Lorem ipsum dolor sit amet, consec.</li>
      <li><svg width="15" height="12" viewBox="0 0 15 12"><path d="M1 6.5 L5.5 10.5 L14 1.5" fill="none" stroke="#f45f3c" stroke-width="3" stroke-linecap="round" stroke-linejoin="round"/></svg>sed diam nonummy nibh euismod.</li>
      <li><svg width="15" height="12" viewBox="0 0 15 12"><path d="M1 6.5 L5.5 10.5 L14 1.5" fill="none" stroke="#f45f3c" stroke-width="3" stroke-linecap="round" stroke-linejoin="round"/></svg>Lorem ipsum dolor sit amet, consec.</li>
      <li><svg width="15" height="12" viewBox="0 0 15 12"><path d="M1 6.5 L5.5 10.5 L14 1.5" fill="none" stroke="#f45f3c" stroke-width="3" stroke-linecap="round" stroke-linejoin="round"/></svg>sed diam nonummy nibh euismod.</li>
      <li><svg width="15" height="12" viewBox="0 0 15 12"><path d="M1 6.5 L5.5 10.5 L14 1.5" fill="none" stroke="#f45f3c" stroke-width="3" stroke-linecap="round" stroke-linejoin="round"/></svg>Lorem ipsum dolor sit amet, consec.</li>
      <li><svg width="15" height="12" viewBox="0 0 15 12"><path d="M1 6.5 L5.5 10.5 L14 1.5" fill="none" stroke="#f45f3c" stroke-width="3" stroke-linecap="round" stroke-linejoin="round"/></svg>sed diam nonummy nibh euismod.</li>
    </ul>
  </section>

  <footer class="site-footer">
    <p class="copyright">Copyright 2016 Local Election. All rights reserved.</p>
    <a class="donate-button" href="#">Donate Now</a>
  </footer>
</body>
</html>
```